Business Card Design

our business is purchasing, rehabbing and flipping homes. Design a house in the palm of a hand. This card is for a new company based in Georgia. So we buy homes that have been foreclosed, short sales,abandond, old homes and vacant homes.
We help improve the communities that we work in. We would like to see designs that use a black background with green accent and other colors that blend and don't take away from the logo and other important information.

Industry/Entity Type

Business

Contact Information for Business Card

Mavenbrook Holdings
Turning Old Doors Into New Starts
2738 Fenwick Lane
Duluth GA 30418
Office: 678-555-0192
mavenbrookholdingsllc.example

```html
<!DOCTYPE html>
<html lang="en">
<head>
<meta charset="utf-8">
<title>Mavenbrook Holdings — Business Card</title>
<link href="https://fonts.googleapis.com/css2?family=PT+Sans:wght@400;700&display=swap" rel="stylesheet">
<style>
  :root {
    --page: #efefef;
    --card: #1f2321;
    --card-edge: #252a28;
    --green: #07574a;
    --frame: #0b5e4f;
    --cream: #ece2cc;
    --text: #e6e6e6;
    --tagline: #d8dcd9;
  }
  * { margin: 0; padding: 0; box-sizing: border-box; }
  html, body {
    width: 1200px;
    height: 1000px;
    overflow: hidden;
    background: var(--page);
    font-family: "PT Sans", Arial, sans-serif;
  }
  .business-card {
    position: absolute;
    left: 75px;
    top: 200px;
    width: 1050px;
    height: 600px;
    background: linear-gradient(100deg, var(--card) 0%, var(--card-edge) 100%);
    border-radius: 4px;
  }
  .inner-frame {
    position: absolute;
    left: 38px;
    top: 44px;
    width: 970px;
    height: 512px;
    border: 4px solid var(--frame);
  }
  .logo-mark {
    position: absolute;
    left: 50%;
    top: 80px;
    width: 230px;
    height: 230px;
    margin-left: -115px;
    border-radius: 50%;
    background: var(--cream);
  }
  .name-band {
    position: absolute;
    left: 0;
    right: 0;
    top: 304px;
    height: 84px;
    background: var(--green);
    text-align: center;
    color: var(--text);
  }
  .company-name {
    font-size: 40px;
    font-weight: 400;
    letter-spacing: 1px;
    line-height: 44px;
    padding-top: 4px;
  }
  .tagline {
    font-size: 20px;
    letter-spacing: 3px;
    line-height: 26px;
    color: var(--tagline);
    text-transform: uppercase;
  }
  .contact-details {
    position: absolute;
    left: 0;
    right: 0;
    top: 402px;
    text-align: center;
    color: var(--text);
    font-size: 22px;
    line-height: 32px;
    letter-spacing: 0.5px;
  }
  .phone-icon {
    width: 20px;
    height: 18px;
    vertical-align: -2px;
    margin-right: 4px;
  }
</style>
</head>
<body>
  <div class="business-card">
    <div class="inner-frame">
      <div class="logo-mark" role="img" aria-label="Mavenbrook Holdings brand mark"></div>
      <div class="name-band">
        <div class="company-name">MAVENBROOK HOLDINGS</div>
        <div class="tagline">Turning Old Doors Into New Starts</div>
      </div>
      <div class="contact-details">
        <p class="address">2738 Fenwick Lane, Duluth , GA 30418</p>
        <p class="phone">
          <svg class="phone-icon" viewBox="0 0 20 18" aria-hidden="true">
            <path d="M2 6 Q10 0 18 6 L16 8 L13 6.5 L13 5 Q10 4 7 5 L7 6.5 L4 8 Z" fill="#e6e6e6"/>
            <rect x="4" y="9" width="12" height="8" rx="1.5" fill="#e6e6e6"/>
            <circle cx="10" cy="13" r="2" fill="#1f2321"/>
          </svg>: 678-555-0192
        </p>
        <p class="website">www.mavenbrookholdingsllc.example</p>
      </div>
    </div>
  </div>
</body>
</html>
```